Design an attractive wine label for Brell Fine Wines

we need a wine label design, we are an Australian wine exporting company'Brell Fine Wines'. We succeed several pallets in last few months and is going to launch our first container. So it’s time to start our own brands. we will have some wines display in China's shopping mall shelves, so we want to have a catchy label which can attract Chinese eyes immediately. other details you will see in the file i uploaded. The design should include a front and back label.

Target Market(s)

Brell Fine Wines are targeting middle class wine drinkers in 2nd-4th tier Chinese cities.

Colors

Designer to choose colors to be used in the design.

Requirements
Must have
• We’d like something that at first glance is Australian (element, style or color…) but subconsciously connects to the Chinese. Demeanor bearing in mind the demographics targeted across the ranges. We would expect the designs and naming to becoming more formalized as they rise to platinum.
Nice to have
• creative things come out
Should not have
• any dead related word or icon, no number '4' related word or icon, no skull related word or icon, kangaroo (see brand 'Copper vine')

```html
<!DOCTYPE html>
<html lang="en">
<head>
<meta charset="UTF-8">
<title>Brell Fine Wines – Solenne Pinot Noir Labels</title>
<link href="https://fonts.googleapis.com/css2?family=Cinzel:wght@400;500&family=Great+Vibes&display=swap" rel="stylesheet">
<style>
  :root {
    --backdrop: #8c8c8c;
    --label-black: #141414;
    --gold: #c9ad7a;
    --gold-band: #d8b56a;
    --silver-band: #d9d9d9;
    --ice-band: #a9c4d0;
    --ink: #2a2a2a;
    --ink-light: #f2f4f5;
    --crimson: #b5122f;
    --navy: #1b2430;
    --rule-dark: #555;
  }
  * { box-sizing: border-box; margin: 0; padding: 0; }
  html, body {
    width: 801px; height: 1200px; overflow: hidden;
    background: var(--backdrop);
  }
  .canvas {
    position: relative; width: 801px; height: 1200px;
    display: flex; justify-content: center; align-items: center; gap: 25px;
  }
  .label-set {
    display: flex; flex-direction: column; align-items: center; gap: 30px;
  }
  .neck-label {
    width: 110px; height: 58px; background: var(--label-black);
    display: flex; flex-direction: column; align-items: center; justify-content: flex-end;
    padding-bottom: 6px;
  }
  .neck-label .brand {
    font-family: 'Great Vibes', cursive; color: var(--gold); font-size: 20px; line-height: 1;
  }
  .neck-label .gold-stripe {
    width: 100%; height: 6px; margin-top: 6px;
    background: linear-gradient(90deg, #8a6d35, var(--gold-band), #f1dca6, var(--gold-band), #8a6d35);
  }
  .front-label {
    position: relative; width: 230px; height: 323px; background: var(--label-black);
    overflow: hidden;
  }
  .front-label .brand {
    position: absolute; top: 30px; left: 0; right: 0; text-align: center;
    font-family: 'Great Vibes', cursive; color: var(--gold); font-size: 44px; line-height: 1;
  }
  .figures {
    position: absolute; top: 172px; left: 65px; width: 100px; height: 52px;
  }
  .varietal-band {
    position: absolute; left: 0; right: 0; top: 232px; height: 88px;
    display: flex; flex-direction: column; align-items: center; justify-content: center; gap: 4px;
  }
  .varietal-band.silver { background: linear-gradient(90deg, #c4c4c4, var(--silver-band), #ececec, var(--silver-band)); }
  .varietal-band.ice { background: var(--ice-band); }
  .varietal {
    font-family: 'Cinzel', serif; font-size: 15px; letter-spacing: 0.5px; color: var(--ink);
  }
  .vintage {
    display: flex; align-items: center; gap: 6px;
    font-family: 'Cinzel', serif; font-size: 9px; letter-spacing: 1px; color: var(--ink);
  }
  .vintage::before, .vintage::after {
    content: ""; width: 20px; height: 1px; background: currentColor;
  }
  .origin {
    font-family: 'Great Vibes', cursive; font-size: 19px; line-height: 1;
  }
  .silver .origin { color: var(--crimson); }
  .ice .varietal, .ice .vintage { color: var(--ink-light); }
  .ice .origin { color: var(--navy); }

  .feature .varietal-top {
    position: absolute; top: 118px; left: 0; right: 0;
    display: flex; flex-direction: column; align-items: center; gap: 8px;
  }
  .feature .varietal, .feature .vintage { color: var(--ink-light); }
  .feature .figures { top: 170px; }
  .pattern-band {
    position: absolute; left: 0; right: 0; top: 222px; bottom: 0;
  }
</style>
</head>
<body>
<main class="canvas">

  <section class="label-set">
    <div class="neck-label"><span class="brand">Solenne</span><span class="gold-stripe"></span></div>
    <div class="front-label">
      <div class="brand">Solenne</div>
      <svg class="figures" viewBox="0 0 100 52" role="img" aria-label="Silhouettes of five dancing figures in pale grey">
        <rect width="100" height="52" fill="#d6d6d6" rx="3"/>
      </svg>
      <div class="varietal-band silver">
        <span class="varietal">PINOT NOIR</span>
        <span class="vintage">2016</span>
        <span class="origin">Australia</span>
      </div>
    </div>
  </section>

  <section class="label-set">
    <div class="neck-label"><span class="brand">Solenne</span><span class="gold-stripe"></span></div>
    <div class="front-label feature">
      <div class="brand">Solenne</div>
      <div class="varietal-top">
        <span class="varietal">PINOT NOIR</span>
        <span class="vintage">2016</span>
      </div>
      <svg class="figures" viewBox="0 0 100 52" role="img" aria-label="Dancing figures in red dot-painting style">
        <rect width="100" height="52" fill="#a0281c" rx="3"/>
      </svg>
      <svg class="pattern-band" viewBox="0 0 230 101" preserveAspectRatio="none" role="img" aria-label="Aboriginal-style dot and leaf pattern in red, orange and ochre">
        <defs>
          <linearGradient id="ochre" x1="0" y1="0" x2="1" y2="1">
            <stop offset="0" stop-color="#b8231a"/>
            <stop offset="0.45" stop-color="#e0662a"/>
            <stop offset="0.75" stop-color="#e9a53a"/>
            <stop offset="1" stop-color="#c23a1e"/>
          </linearGradient>
        </defs>
        <rect width="230" height="101" fill="url(#ochre)"/>
      </svg>
    </div>
  </section>

  <section class="label-set">
    <div class="neck-label"><span class="brand">Solenne</span><span class="gold-stripe"></span></div>
    <div class="front-label">
      <div class="brand">Solenne</div>
      <svg class="figures" viewBox="0 0 100 52" role="img" aria-label="Silhouettes of five dancing figures in pale blue">
        <rect width="100" height="52" fill="#9fbccb" rx="3"/>
      </svg>
      <div class="varietal-band ice">
        <span class="varietal">PINOT NOIR</span>
        <span class="vintage">2016</span>
        <span class="origin">Australia</span>
      </div>
    </div>
  </section>

</main>
</body>
</html>
```